Personal Finance Blog Wordpress Design

We are looking for a new Wordpress theme design for CoinHarborly.com.

All of the elements that are currently on the homepage should remain, minus the archives list. The placement of various elements can be changed, we just need a more modern and clean feel. We would like to add a 160 x 600 ad unit on the homepage. We would like the 728x90 ad to be below the navigation similar to that of: http://www.plumtreeledger.org/blog/

We like the fonts used on: http://www.quillpocket.com/blog/

The text that currently resides at the bottom of CoinHarborly.com needs to remain on the homepage, but wherever it is placed needs to not be intrusive.

The color scheme needs to appropriately compliment the logo.

No sliders. I don't like sliders.

I am happy to answer questions.

Industry/Entity Type

Finance

Requirements
Must have
• Included in project description
Nice to have
Should not have
• Included in project description. Don't use sliders

```html
<!DOCTYPE html>
<html lang="en">
<head>
<meta charset="utf-8">
<title>Coin Harborly – Personal Finance Blog</title>
<link rel="stylesheet" href="https://fonts.googleapis.com/css2?family=Rokkitt:wght@400;600;700&family=Roboto:wght@300;400&display=swap">
<style>
:root{
  --green-dark:#1f6a1c;
  --green-title:#1d5e12;
  --lime:#7fb51a;
  --lime-dark:#5f9a10;
  --text:#444;
  --muted:#666;
  --border:#d6d6d6;
  --dash:#9a9a9a;
}
*{box-sizing:border-box;margin:0;padding:0}
html,body{width:1014px;height:1200px;overflow:hidden;background:#fff}
body{position:relative;font-family:"Roboto",Arial,sans-serif;font-weight:300;color:var(--text);font-size:10px}
.abs{position:absolute}
.top-rule{left:0;top:0;width:1014px;height:3px;background:var(--lime)}
.logo{left:64px;top:22px;display:flex;align-items:center;gap:6px;font-family:"Roboto",sans-serif;font-weight:400;font-size:17px;color:var(--green-dark)}
.logo-mark{width:28px;height:28px;border-radius:50%;background:#c9cfc6}
.social{top:24px;width:25px;height:25px;border-radius:2px}
.search{left:747px;top:20px;width:203px;height:32px;border:1px solid #cfcfcf;border-radius:2px}
.search span{position:absolute;left:10px;top:9px;font-style:italic;color:#999;font-size:10px}
.search-btn{right:0;top:0;width:31px;height:30px;background:var(--lime)}
.nav{left:63px;top:69px;width:887px;height:35px;background:var(--green-dark);display:flex;align-items:center;border-radius:1px;overflow:hidden}
.nav a{flex:1 1 auto;text-align:center;color:#fff;text-decoration:none;font-family:"Rokkitt",serif;font-size:10.5px;letter-spacing:.3px;padding:0 6px;height:35px;line-height:35px;border-right:1px solid #2f7d2b;white-space:nowrap}
.nav a:last-child{border-right:none}
.ad{display:flex;align-items:center;justify-content:center;color:#fff}
.banner{left:160px;top:112px;width:567px;height:70px;background:linear-gradient(90deg,#2a2a3e,#3a3448 55%,#4c4058);flex-direction:column;align-items:flex-end;padding-right:6px;font-family:"Roboto",sans-serif;font-weight:400}
.banner .name{position:absolute;left:8px;top:8px;font-family:"Rokkitt",serif;font-size:24px}
.banner .url{font-size:13px;line-height:18px;margin-top:auto}
.banner .url:last-child{margin-top:0;margin-bottom:4px}
.sky{left:826px;top:112px;width:124px;height:468px;background:linear-gradient(180deg,#17408a 0 70%,#7cb427 70%);flex-direction:column;justify-content:flex-start;padding:40px 8px 0;font-family:"Roboto",sans-serif;font-weight:400;text-align:left;align-items:flex-start}
.sky .big{font-size:38px;line-height:36px}
.sky .mid{font-size:13px;line-height:15px;margin-top:8px}
.sky .date{font-size:20px;color:#f2c400;margin-top:90px}
.sky .small{font-size:10px;line-height:12px}
.sky .foot{margin-top:64px;font-size:9px;text-align:center;width:100%}
.sky .foot b{display:block;font-size:22px;font-weight:400}
.box{border:1px solid var(--border);background:#fff}
.h-slab{font-family:"Rokkitt",serif;color:var(--green-title);font-weight:600}
.photo{border-radius:1px}
.meta{display:flex;align-items:center;gap:6px;font-size:10px;color:var(--lime);font-weight:400;font-family:"Roboto",sans-serif;white-space:nowrap}
.meta b{color:#333;font-weight:400}
.meta svg{flex:none}
.btn{background:var(--lime);color:#fff;font-family:"Roboto",sans-serif;font-weight:400;font-size:9px;letter-spacing:.3px;display:flex;align-items:center;justify-content:center;border-bottom:2px solid var(--lime-dark);border-radius:1px}
.post-card{left:431px;width:338px;height:114px;border:1px solid var(--border)}
.post-card .thumb{position:absolute;left:13px;top:15px;width:79px;height:75px}
.post-card h3{position:absolute;left:103px;top:13px;width:225px;font-family:"Rokkitt",serif;font-weight:600;color:var(--green-title);font-size:14px;line-height:18px}
.post-card p{position:absolute;left:103px;top:52px;width:200px;font-size:10px;line-height:16px;color:var(--muted)}
.post-card .meta{position:absolute;left:103px;top:86px}
.excerpt{font-size:10.5px;line-height:17px;color:var(--muted)}
.sidebar-list{list-style:none}
.sidebar-list li{font-size:10px;line-height:15px;color:#555;padding:7px 0 9px 13px;border-bottom:1px dashed var(--dash);position:relative}
.sidebar-list li:last-child{border-bottom:none}
.sidebar-list li::before{content:"››";position:absolute;left:0;top:7px;font-size:9px}
.footer{left:0;top:1084px;width:1014px;height:116px;background:linear-gradient(180deg,#e4e4e4,#fbfbfb)}
.footer-links{position:absolute;top:27px;width:100%;text-align:center;font-size:10.5px;color:#444;font-weight:400}
.footer-links span{color:#888;margin:0 7px}
.footer-note{position:absolute;width:100%;text-align:center;font-size:9.5px;color:#666}
</style>
</head>
<body>

<div class="abs top-rule"></div>

<header>
  <div class="abs logo"><span class="logo-mark"></span>CoinHarborly</div>
  <div class="abs social" style="left:615px;background:#3b5998" aria-label="Social link one"></div>
  <div class="abs social" style="left:646px;background:#2aa9e0" aria-label="Social link two"></div>
  <div class="abs social" style="left:677px;background:#d73d32" aria-label="Social link three"></div>
  <div class="abs social" style="left:709px;background:#f28a1c" aria-label="Feed link"></div>
  <div class="abs search">
    <span>Search...</span>
    <div class="abs search-btn">
      <svg width="31" height="30" viewBox="0 0 31 30"><circle cx="17.5" cy="12.5" r="5" fill="none" stroke="#fff" stroke-width="2"/><line x1="14" y1="16" x2="9.5" y2="20.5" stroke="#fff" stroke-width="3" stroke-linecap="round"/></svg>
    </div>
  </div>
  <nav class="abs nav">
    <a>AUTO</a><a>BANK ACCOUNTS »</a><a>CD RATES</a><a>CREDIT CARDS</a><a>INSURANCE</a><a>INVESTMENTS »</a><a>MORTGAGES</a><a>PERSONAL FINANCE</a><a>SMALL BUSINESS</a><a>TAXES</a>
  </nav>
</header>

<div class="abs ad banner" role="img" aria-label="Leaderboard advert: night city skyline">
  <span class="name">Harbor Lane Story Writers</span>
  <span class="url">www.hlswriters.com</span>
  <span class="url">www.harborlanestorywriters.com</span>
</div>

<div class="abs ad sky" role="img" aria-label="Skyscraper advert for an earthquake drill">
  <div class="big">Join<br>Us</div>
  <div class="mid">for the Largest<br>Earthquake Drill<br>in U.S. History.</div>
  <div class="date">11.13.08</div>
  <div class="small">Register Now at<br>www.rumbleready.org</div>
  <div class="foot">The Great Coastal<b>Rumble Ready</b></div>
</div>

<section class="abs box" style="left:76px;top:198px;width:735px;height:401px">
  <h2 class="abs h-slab" style="left:3px;top:17px;font-size:18px;color:#222;font-weight:400">RECENT POST</h2>
  <div class="abs photo" style="left:3px;top:50px;width:340px;height:186px;background:linear-gradient(135deg,#6d6a66,#b7b2ab 45%,#8a8580)" role="img" aria-label="Photo: hands holding tablets and phones showing furniture"></div>
  <h3 class="abs h-slab" style="left:3px;top:248px;font-size:18px">Best Budgeting Software for 2015</h3>
  <p class="abs excerpt" style="left:3px;top:272px;width:330px">As businesses everywhere look to find new and more efficient ways to develop their budgets in 2015, much of their attention is focused on finding...</p>
  <div class="abs btn" style="left:3px;top:355px;width:80px;height:27px">READ MORE</div>
  <div class="abs meta" style="left:98px;top:362px">
    <svg width="16" height="14" viewBox="0 0 16 14"><rect x="1" y="1.5" width="14" height="12" fill="none" stroke="#999"/><line x1="1" y1="4.5" x2="15" y2="4.5" stroke="#999"/><g fill="#aaa"><rect x="3" y="6.5" width="2" height="1.5"/><rect x="7" y="6.5" width="2" height="1.5"/><rect x="11" y="6.5" width="2" height="1.5"/><rect x="3" y="9.5" width="2" height="1.5"/><rect x="7" y="9.5" width="2" height="1.5"/><rect x="11" y="9.5" width="2" height="1.5"/></g></svg>
    APR 28, 2015&nbsp;&nbsp;&nbsp;&nbsp;
    <svg width="20" height="13" viewBox="0 0 20 13"><path d="M10 1.5c4.5 0 8 2 8 4.5s-3.5 4.5-8 4.5c-1 0-2 0-2.8-.3L3.5 12l1.2-2.6C3 8.6 2 7.4 2 6c0-2.5 3.5-4.5 8-4.5z" fill="none" stroke="#999"/></svg>
    COMMENTS <b>0</b>
  </div>
  <div class="abs" style="left:711px;top:22px;width:8px;height:34px;background:#666"></div>
</section>

<article class="abs post-card" style="top:220px">
  <div class="thumb" style="background:radial-gradient(circle,#2357c9,#0b2a7a)" role="img" aria-label="Satellite radio brand artwork"></div>
  <h3>Stellarwave Radio Stock: How it Fares in 2015</h3>
  <p>As the days of satellite radio seem to be numbered, there seems to...</p>
  <div class="meta">
    <svg width="16" height="14" viewBox="0 0 16 14"><rect x="1" y="1.5" width="14" height="12" fill="none" stroke="#999"/><line x1="1" y1="4.5" x2="15" y2="4.5" stroke="#999"/></svg>
    APR 28, 2015&nbsp;&nbsp;&nbsp;&nbsp;
    <svg width="20" height="13" viewBox="0 0 20 13"><path d="M10 1.5c4.5 0 8 2 8 4.5s-3.5 4.5-8 4.5c-1 0-2 0-2.8-.3L3.5 12l1.2-2.6C3 8.6 2 7.4 2 6c0-2.5 3.5-4.5 8-4.5z" fill="none" stroke="#999"/></svg>
    COMMENTS <b>0</b>
  </div>
</article>
<article class="abs post-card" style="top:342px">
  <div class="thumb" style="background:linear-gradient(160deg,#8c5a44,#b98e74 50%,#d6d0c6)" role="img" aria-label="Photo: house with a foreclosure sale sign"></div>
  <h3>Stellarwave Radio Stock: How it Fares in 2015</h3>
  <p>As the days of satellite radio seem to be numbered, there seems to...</p>
  <div class="meta">
    <svg width="16" height="14" viewBox="0 0 16 14"><rect x="1" y="1.5" width="14" height="12" fill="none" stroke="#999"/><line x1="1" y1="4.5" x2="15" y2="4.5" stroke="#999"/></svg>
    APR 28, 2015&nbsp;&nbsp;&nbsp;&nbsp;
    <svg width="20" height="13" viewBox="0 0 20 13"><path d="M10 1.5c4.5 0 8 2 8 4.5s-3.5 4.5-8 4.5c-1 0-2 0-2.8-.3L3.5 12l1.2-2.6C3 8.6 2 7.4 2 6c0-2.5 3.5-4.5 8-4.5z" fill="none" stroke="#999"/></svg>
    COMMENTS <b>0</b>
  </div>
</article>
<article class="abs post-card" style="top:463px">
  <div class="thumb" style="background:linear-gradient(135deg,#f3f3f1,#d9d3c8 60%,#b44 100%)" role="img" aria-label="Illustration: rising red arrow over stacks of money"></div>
  <h3>Stellarwave Radio Stock: How it Fares in 2015</h3>
  <p>As the days of satellite radio seem to be numbered, there seems to...</p>
  <div class="meta">
    <svg width="16" height="14" viewBox="0 0 16 14"><rect x="1" y="1.5" width="14" height="12" fill="none" stroke="#999"/><line x1="1" y1="4.5" x2="15" y2="4.5" stroke="#999"/></svg>
    APR 28, 2015&nbsp;&nbsp;&nbsp;&nbsp;
    <svg width="20" height="13" viewBox="0 0 20 13"><path d="M10 1.5c4.5 0 8 2 8 4.5s-3.5 4.5-8 4.5c-1 0-2 0-2.8-.3L3.5 12l1.2-2.6C3 8.6 2 7.4 2 6c0-2.5 3.5-4.5 8-4.5z" fill="none" stroke="#999"/></svg>
    COMMENTS <b>0</b>
  </div>
</article>

<section class="abs box" style="left:63px;top:619px;width:584px;height:235px">
  <div class="abs" style="left:15px;top:16px;width:71px;height:29px;background:var(--lime);color:#fff;font-family:'Rokkitt',serif;font-weight:700;font-size:13px;letter-spacing:.5px;display:flex;align-items:center;justify-content:center">AUTO</div>
  <div class="abs" style="left:15px;top:44px;width:550px;height:2px;background:var(--lime)"></div>
  <svg class="abs" style="left:535px;top:9px" width="40" height="18" viewBox="0 0 40 18"><path d="M10 3l-6 6 6 6M27 3l6 6-6 6" fill="none" stroke="#333" stroke-width="1.6"/></svg>
  <div class="abs photo" style="left:15px;top:68px;width:186px;height:143px;background:linear-gradient(135deg,#6b6b6b,#a8a8a8 50%,#4f4f4f)" role="img" aria-label="Photo: parked cars behind a fuel gauge"></div>
  <h3 class="abs h-slab" style="left:218px;top:73px;font-size:18px">7 Cars With Good Gas Mileage</h3>
  <p class="abs excerpt" style="left:218px;top:95px;width:340px">Fuel efficient vehicles can save you money, reduce the need to stop for gas as often, and benefit the environment. In many cases, it is true that you will pay more for the vehicle itself, but if the miles per gallon is sufficiently higher, you will still come out ahead. This is especially true if you travel a large number of miles per year.</p>
  <div class="abs btn" style="left:218px;top:186px;width:80px;height:27px">READ MORE</div>
  <div class="abs meta" style="left:313px;top:192px">
    <svg width="16" height="14" viewBox="0 0 16 14"><rect x="1" y="1.5" width="14" height="12" fill="none" stroke="#999"/><line x1="1" y1="4.5" x2="15" y2="4.5" stroke="#999"/></svg>
    APR 28, 2015&nbsp;&nbsp;&nbsp;&nbsp;
    <svg width="20" height="13" viewBox="0 0 20 13"><path d="M10 1.5c4.5 0 8 2 8 4.5s-3.5 4.5-8 4.5c-1 0-2 0-2.8-.3L3.5 12l1.2-2.6C3 8.6 2 7.4 2 6c0-2.5 3.5-4.5 8-4.5z" fill="none" stroke="#999"/></svg>
    COMMENTS <b>0</b>
  </div>
</section>

<aside class="abs box" style="left:671px;top:619px;width:279px;height:235px">
  <h2 class="abs h-slab" style="left:17px;top:16px;font-size:21px">RECENT POSTS</h2>
  <ul class="abs sidebar-list" style="left:17px;top:47px;width:250px">
    <li>Best Budgeting Software for 2015</li>
    <li>Stellarwave Radio Stock: How it Fares in 2015</li>
    <li>Financial Benefits of Buying Foreclosed Homes</li>
    <li>Want to Increase Your Savings? Check Out These Great Saving Money Tips.</li>
    <li>5 Appliances on Sale to Save Money</li>
  </ul>
</aside>

<section class="abs" style="left:63px;top:876px;width:590px">
  <h2 class="h-slab" style="font-size:21px">ABOUT COIN HARBORLY: PERSONAL FINANCE BLOG</h2>
  <p style="margin-top:10px;font-size:10px;line-height:20px;color:#555">Our mission is to enrich the lives of our readers (literally!) by providing the very best personal finance content on the internet. Our readers may be at different stages in life, with different personal finance situations and needs: One person may be looking to get their first credit card, another might be looking into how to get a mortgage to buy a home, some may be looking for ways to afford or finance a college education for themselves or their children, many want to know how to improve their credit score, and still others might be planning for retirement.</p>
</section>
<div class="abs btn" style="left:63px;top:1035px;width:80px;height:27px">READ MORE</div>

<aside class="abs box" style="left:671px;top:883px;width:279px;height:178px">
  <h2 class="abs h-slab" style="left:17px;top:16px;font-size:21px">E-MAIL NEWSLETTER</h2>
  <p class="abs" style="left:17px;top:47px;width:250px;font-size:10px;line-height:16px;color:#555">Sign up now to receive breaking news and to hear what's new with our website!</p>
  <div class="abs" style="left:18px;top:86px;width:240px;height:34px;border:1px solid #cfcfcf"><span class="abs" style="left:12px;top:11px;font-style:italic;color:#888">Enter Email Address</span></div>
  <div class="abs btn" style="left:186px;top:133px;width:69px;height:28px;font-size:10px">SUBMIT</div>
</aside>

<footer class="abs footer">
  <div class="footer-links">Home<span>/</span>Personal Finance<span>/</span>Mortgages<span>/</span>Bank Accounts<span>/</span>Credit Cards<span>/</span>Insurance<span>/</span>Auto<span>/</span>Investments<span>/</span>Taxes<span>/</span>Small Business</div>
  <div class="footer-note" style="top:56px">Copyright © 2015 Coin Harborly. All rights reserved. | Contact Us</div>
  <div class="footer-note" style="top:76px">Privacy Policy | Terms and Conditions</div>
</footer>

</body>
</html>
```